Business Card Design Project

New business cards that encompass our new logo.
Looking for -
Name, Title, Cell Phone, Email, Address (2 lines), Main Phone, Fax, and website.
Reason: I don't like the graphics used to show phone, fax, cell, email, web, and address.....
I like the double sided cards with logo's on the back. I do not like the logos for phone, fax, cell, address, email, or web.

```html
<!DOCTYPE html>
<html lang="en">
<head>
<meta charset="utf-8">
<title>Tundra Kitchen Supply – Business Card</title>
<link href="https://fonts.googleapis.com/css2?family=Carlito:wght@400;700&family=Open+Sans:wght@400;600&display=swap" rel="stylesheet">
<style>
  :root {
    --navy: #1d4482;
    --red: #b3313f;
    --card-light: #ececec;
    --ink: #1a1a1a;
    --backdrop: #dcdde0;
  }
  * { box-sizing: border-box; margin: 0; padding: 0; }
  html, body {
    width: 1200px; height: 934px; overflow: hidden;
    background: var(--backdrop);
  }
  .sheet {
    width: 1200px; height: 934px;
    display: flex; align-items: center; justify-content: center; gap: 40px;
  }
  .card {
    position: relative;
    width: 560px; height: 320px;
    overflow: hidden;
  }
  /* back side */
  .card--back {
    background: var(--navy);
    display: flex; align-items: center; justify-content: center;
  }
  .card--back .brand-name {
    font-family: "Open Sans", sans-serif;
    font-weight: 600;
    font-size: 40px;
    letter-spacing: 1px;
    color: #ffffff;
    text-align: center;
    line-height: 1.15;
  }
  .card--back .brand-name span { display: block; font-size: 22px; letter-spacing: 5px; }
  /* front side */
  .card--front { background: var(--card-light); }
  .card--front .brand-name {
    position: absolute; left: 48px; top: 46px;
    font-family: "Open Sans", sans-serif;
    font-weight: 600;
    color: var(--navy);
    font-size: 38px;
    line-height: 1.05;
  }
  .card--front .brand-name span { display: block; font-size: 17px; letter-spacing: 3px; }
  .person {
    position: absolute; left: 48px; top: 140px;
    font-family: "Open Sans", sans-serif;
    font-size: 15px; letter-spacing: 1.5px;
    color: var(--navy);
  }
  .person .divider { color: var(--navy); margin: 0 6px; }
  .person .role { color: var(--red); letter-spacing: 0.5px; }
  .contact {
    position: absolute; left: 48px; top: 182px;
    font-family: "Carlito", sans-serif;
    font-size: 14px; line-height: 1.3;
    color: var(--ink);
  }
  .contact .label { color: var(--navy); }
  .contact .sep { margin: 0 4px; }
  .address {
    position: absolute; left: 48px; top: 250px;
    font-family: "Carlito", sans-serif;
    font-size: 14px; color: var(--ink);
  }
  .band { position: absolute; left: 0; bottom: 0; }
</style>
</head>
<body>
<main class="sheet">
  <section class="card card--back" aria-label="Card back">
    <p class="brand-name">TUNDRA<span>KITCHEN SUPPLY</span></p>
  </section>

  <section class="card card--front" aria-label="Card front">
    <p class="brand-name">TUNDRA<span>KITCHEN SUPPLY</span></p>
    <p class="person">EMPLOYEE NAME<span class="divider">|</span><span class="role">Founder/CEO</span></p>
    <div class="contact">
      <p><span class="label">phone:</span> 907.555.0142<span class="sep">|</span><span class="label">toll free:</span> 855.555.0190<span class="sep">|</span><span class="label">fax:</span> 907.555.0177</p>
      <p><span class="label">Email:</span> info@tundrakitchensupply.com<span class="sep">|</span><span class="label">Web:</span> www.tundrakitchensupply.com</p>
    </div>
    <p class="address">1480 Harbor Lane, Kenai Point, AK 99500</p>
    <svg class="band" width="560" height="320" viewBox="0 0 560 320" aria-hidden="true">
      <polygon points="0,300 560,230 560,320 0,320" fill="var(--navy)"/>
    </svg>
  </section>
</main>
</body>
</html>
```